Buchcover-Design für Fragenbuch
Ganz herzlichen Dank. Die Zusammenarbeit war völlig reibungslos und entspannt. Änderungswünsche wurden professionell umgesetzt und die kreativen Vorschläge fand ich super. Ich bin total glücklich mit dem Ergebnis.
Zielgruppe
Autorin und Workshopleiterin. Zielgruppe: Frauen ab 30
Aufgabenstellung
Ich benötige ein komplettes Buchcover, sowie 12 farbige Innenseiten. Es geht um ein Fragenbuch zum Ausfüllen mit dem Titel:
„Finde zurück zur leisen Mitte
Ein Arbeitsheft zum Eintragen für tiefere seelische Ruhe“
Das Format des Buches beträgt 17x22cm. Es ist in 12 Wochen unterteilt. Darum hätte ich gerne zwischen den einzelnen Wochen eine farbige Seite (1. Woche, 2. Woche etc.), die designmäßig mit dem Außencover korrespondiert.
Die Farben sollten eher zart oder gedeckt sein. Auf keinen Fall jedoch kitschig. Wichtig ist mir, dass keine bestimmte Person zu sehen ist. (Foto)
Das ist meine Website www.finde-zurueck-zur-leisen-mitte.de

```html
<!DOCTYPE html>
<html lang="de">
<head>
<meta charset="utf-8">
<title>Finde zurück zur leisen Mitte – Cover und Wochenseite</title>
<link rel="stylesheet" href="https://fonts.googleapis.com/css2?family=Jost:wght@300&family=EB+Garamond:wght@500&family=Open+Sans:wght@400&family=Mrs+Saint+Delafield&display=swap">
<style>
  :root {
    --canvas: #ffffff;
    --page: #e7dbcf;
    --frame: #b9a089;
    --frame-inner: #f3ede7;
    --ink: #4a362c;
    --rule: #cbb9a8;
    --photo-light: #f1e4d3;
    --photo-mid: #dcc3a6;
    --photo-dark: #8a5e3f;
  }
  * { margin: 0; padding: 0; box-sizing: border-box; }
  html, body {
    width: 1200px; height: 849px; overflow: hidden;
    background: var(--canvas);
  }
  .spread { position: relative; width: 1200px; height: 849px; }
  .page {
    position: absolute; top: 176px;
    width: 368px; height: 476px;
    background: var(--page);
    overflow: hidden;
    color: var(--ink);
  }
  .page--cover { left: 233px; }
  .page--week { left: 656px; }
  .page svg.shapes { position: absolute; inset: 0; }

  .cover-title {
    position: absolute; left: 0; top: 0;
    font-family: "Jost", sans-serif; font-weight: 300;
    font-size: 37px; line-height: 1; letter-spacing: 0.5px;
    text-transform: uppercase;
  }
  .cover-title span { position: absolute; white-space: nowrap; }
  .cover-title .l1 { left: 51px; top: 34px; }
  .cover-title .l2 { left: 70px; top: 66px; }
  .cover-title .l3 { left: 17px; top: 99px; }
  .cover-title .l4 { left: 27px; top: 131px; }

  .portrait-area {
    position: absolute; left: 102px; top: 126px;
    width: 158px; height: 158px; border-radius: 50%;
    background: radial-gradient(circle at 50% 45%, #c9b2a0 0%, #8d8478 55%, #5c4a42 100%);
  }

  .centered { position: absolute; left: 0; width: 100%; text-align: center; }
  .cover-subtitle-main {
    top: 326px; left: -3px;
    font-family: "EB Garamond", serif; font-weight: 500;
    font-size: 22px; letter-spacing: 0.8px; text-transform: uppercase;
  }
  .cover-subtitle-small {
    top: 355px; left: -3px;
    font-family: "Open Sans", sans-serif; font-size: 10px;
  }
  .cover-author {
    top: 386px; left: -3px;
    font-family: "Mrs Saint Delafield", cursive; font-size: 26px;
  }

  .week-number {
    position: absolute; left: 30px; top: 32px;
    font-family: "Jost", sans-serif; font-weight: 300;
    font-size: 122px; line-height: 1;
  }
  .week-label {
    position: absolute; left: 34px; top: 136px;
    font-family: "Jost", sans-serif; font-weight: 300;
    font-size: 36px; line-height: 1; text-transform: uppercase;
  }
  .module-kicker {
    top: 300px;
    font-family: "Open Sans", sans-serif; font-size: 10.5px;
    text-transform: uppercase;
  }
  .module-title {
    top: 325px;
    font-family: "EB Garamond", serif; font-weight: 500;
    font-size: 22px; letter-spacing: 0.6px; text-transform: uppercase;
  }
  .module-rule {
    position: absolute; left: 136px; top: 365px;
    width: 94px; height: 1px; background: var(--rule);
  }
</style>
</head>
<body>
<main class="spread">

  <section class="page page--cover" aria-label="Buchcover">
    <svg class="shapes" width="368" height="476" viewBox="0 0 368 476">
      <path fill="var(--frame)" d="M49 70 H312 Q318 70 318 76 V263 Q318 338 243 338 H49 Z"/>
      <path fill="var(--frame-inner)" d="M82 103 H285 V255 Q285 305 235 305 H82 Z"/>
    </svg>
    <div class="portrait-area" role="img" aria-label="Rundes Porträtfoto vor heller Steinwand"></div>
    <h1 class="cover-title">
      <span class="l1">Finde</span>
      <span class="l2">zurück</span>
      <span class="l3">zur leisen</span>
      <span class="l4">Mitte</span>
    </h1>
    <p class="centered cover-subtitle-main">Ein Arbeitsheft</p>
    <p class="centered cover-subtitle-small">zum Eintragen für tiefere seelische Ruhe</p>
    <p class="centered cover-author">by Mira Lindholt</p>
  </section>

  <section class="page page--week" aria-label="Wochenseite">
    <svg class="shapes" width="368" height="476" viewBox="0 0 368 476">
      <defs>
        <linearGradient id="photoTone" x1="0" y1="0" x2="1" y2="1">
          <stop offset="0" stop-color="var(--photo-mid)"/>
          <stop offset="0.5" stop-color="var(--photo-light)"/>
          <stop offset="1" stop-color="var(--photo-mid)"/>
        </linearGradient>
      </defs>
      <path fill="var(--frame)" d="M175 48 Q175 0 223 0 H369 V170 Q369 200 339 200 H175 Z"/>
      <path fill="url(#photoTone)" role="img" aria-label="Foto mit halbierten Kokosnüssen auf hellem Grund"
            d="M187 40 Q187 0 227 0 H369 V166 Q369 188 347 188 H187 Z"/>
    </svg>
    <div class="week-number">2</div>
    <div class="week-label">Woche</div>
    <p class="centered module-kicker">Title or headline here</p>
    <h2 class="centered module-title">Your Module</h2>
    <div class="module-rule"></div>
  </section>

</main>
</body>
</html>
```